Educational Construction Organization needs Flyer for Upcoming Forum

We need a SAVE THE DATE Flyer for our 2020 BemTK Forum. We work with Architects, Engineers, Contractors and Owners in the design and construction industry. Our mission is to evolve the capital projects industry through sharing of knowledge for optimized leadership, delivery and performance. The final design should communicate the connection between these industry professionals, our mission, and the Forum theme and byline.
Updates

Target Market(s)

Design and construction industry.

Industry/Entity Type

Construction

Font styles to use
Sans Serif

Colors

Designer to choose colors to be used in the design.

Requirements
Must have
• Title, By-line, 3 key topics, Date and location. Design that implements the theme with graphic(s) (not just text).
• NEW TITLE: FUTURE PROOFING: Connecting the dots to make sense of the "SMART" City
• 3 Key Topics: Smart Cities, Smart Institutions, Smart Connections
• Date: April 1-3, 2020
• Location: San Antonio, TX
Nice to have
• Please review attached problem statement for a better understanding of what this Forum will focus on when designing your graphic for the flyer.

```html
<!DOCTYPE html>
<html lang="en">
<head>
<meta charset="utf-8">
<title>2020 BemTK Forum – Save the Date</title>
<link rel="stylesheet" href="https://fonts.googleapis.com/css2?family=Montserrat:wght@300;400;500;600;700;800;900&display=swap">
<style>
  :root {
    --navy: #1e3f94;
    --navy-deep: #16307a;
    --green: #8db03f;
    --green-text: #88ad38;
    --grey-text: #4a4a4a;
    --column-grey: #e6e7e9;
    --paper: #ffffff;
    --paper-shade: #eef0f0;
  }
  * { margin: 0; padding: 0; box-sizing: border-box; }
  html, body { width: 848px; height: 1200px; overflow: hidden; background: #ffffff; }
  body { font-family: "Montserrat", sans-serif; }

  .flyer {
    position: relative; width: 848px; height: 1200px; overflow: hidden;
    background: linear-gradient(135deg, var(--paper) 0%, var(--paper-shade) 45%, var(--paper) 70%, var(--paper-shade) 100%);
  }

  .hero {
    position: absolute; left: 0; top: 0; width: 848px; height: 254px;
    background: linear-gradient(180deg, #3a3fc4 0%, #2b2fa8 45%, #3b1f86 80%, #5a2a9a 100%);
  }
  .hero-title {
    position: absolute; left: 90px; top: 70px;
    color: #fff; font-weight: 900; font-size: 60px; line-height: 56px; letter-spacing: -1px;
    text-shadow: 4px 3px 0 var(--navy-deep);
  }

  .topic-column {
    position: absolute; left: 630px; top: 239px; width: 166px; height: 643px;
    background: var(--column-grey);
  }
  .topic { position: absolute; left: 0; width: 166px; text-align: center; color: var(--navy); }
  .topic-label { font-size: 19px; font-weight: 500; line-height: 23px; }
  .topic-icon { display: block; margin: 0 auto 16px; }
  .topic-icon.placeholder { border-radius: 6px; background: linear-gradient(180deg, #c9cfe3, #aab5d8); }

  .headline { position: absolute; left: 80px; top: 262px; color: var(--navy); }
  .headline-line { font-size: 67px; font-weight: 300; line-height: 67px; letter-spacing: 0; white-space: nowrap; }
  .headline-line.strong { font-weight: 900; letter-spacing: -1px; }

  .byline {
    position: absolute; left: 85px; top: 474px; color: var(--green-text);
    font-size: 23px; font-weight: 800; line-height: 25px; text-transform: uppercase; letter-spacing: -0.2px;
  }

  .intro {
    position: absolute; left: 72px; top: 562px; width: 560px;
    color: var(--grey-text); font-size: 19.5px; font-weight: 700; line-height: 30px;
  }
  .questions { position: absolute; left: 67px; top: 622px; width: 560px; list-style: none; }
  .questions li {
    position: relative; padding-left: 26px; color: var(--grey-text);
    font-size: 19.5px; font-weight: 400; line-height: 30px;
  }
  .questions .num {
    position: absolute; left: 0; top: 6px; width: 20px; height: 20px; border-radius: 50%;
    background: var(--navy); color: #fff; font-size: 9px; font-weight: 700;
    display: flex; align-items: center; justify-content: center;
  }

  .event-band {
    position: absolute; left: 53px; top: 882px; width: 743px; height: 116px;
    background: var(--green); display: flex; align-items: center;
  }
  .event-invite {
    position: absolute; left: 56px; top: 30px; width: 240px;
    color: var(--navy); font-size: 16.5px; font-weight: 700; line-height: 20px;
  }
  .event-item { position: absolute; top: 32px; display: flex; align-items: center; gap: 16px; color: #fff; font-size: 20px; font-weight: 700; line-height: 22px; }
  .event-date { left: 306px; }
  .event-place { left: 554px; }

  .org-mark { position: absolute; left: 224px; top: 1040px; display: flex; align-items: center; gap: 26px; }
  .org-dot { width: 96px; height: 96px; border-radius: 50%; background: var(--navy); }
  .org-name { color: #555; font-size: 66px; font-weight: 400; letter-spacing: -1px; line-height: 1; }

  .site-bar {
    position: absolute; left: 0; top: 1148px; width: 848px; height: 52px; background: var(--navy);
    color: #fff; font-size: 20px; font-weight: 800; letter-spacing: 8px;
    display: flex; align-items: center; justify-content: center;
  }
</style>
</head>
<body>
<main class="flyer">
  <header class="hero" role="img" aria-label="Night city skyline with lit towers and fireworks in blue and purple tones">
    <h1 class="hero-title">2020 BEMTK<br>FORUM</h1>
  </header>

  <aside class="topic-column">
    <div class="topic" style="top:62px">
      <div class="topic-icon placeholder" role="img" aria-label="Line drawing of a city skyline" style="width:80px;height:74px"></div>
      <p class="topic-label">SMART<br>Cities</p>
    </div>
    <div class="topic" style="top:240px">
      <div class="topic-icon placeholder" role="img" aria-label="Line drawing of an institutional building with a flag" style="width:80px;height:92px"></div>
      <p class="topic-label">SMART<br>Institutions</p>
    </div>
    <div class="topic" style="top:430px">
      <svg class="topic-icon" width="110" height="100" viewBox="0 0 110 100" aria-hidden="true">
        <g stroke="var(--navy)" stroke-width="5" stroke-linecap="round">
          <line x1="55" y1="50" x2="27" y2="28"/><line x1="55" y1="50" x2="82" y2="14"/>
          <line x1="55" y1="50" x2="14" y2="68"/><line x1="55" y1="50" x2="98" y2="54"/>
          <line x1="55" y1="50" x2="62" y2="88"/>
        </g>
        <g fill="var(--navy)">
          <circle cx="55" cy="50" r="16"/><circle cx="24" cy="24" r="9"/><circle cx="84" cy="12" r="9"/>
          <circle cx="12" cy="69" r="8"/><circle cx="100" cy="54" r="8"/><circle cx="63" cy="91" r="8"/>
        </g>
      </svg>
      <p class="topic-label">SMART<br>Connections</p>
    </div>
  </aside>

  <h2 class="headline">
    <span class="headline-line" style="display:block">MAKING</span>
    <span class="headline-line" style="display:block">SENSE OF THE</span>
    <span class="headline-line strong" style="display:block">SMART CITY</span>
  </h2>

  <p class="byline">Connecting the dots for dynamic<br>planning, design &amp; delivery</p>

  <p class="intro">All over the nation, regions, cities and facility Owners are trying to get a handle on being “smart.”</p>
  <ol class="questions">
    <li><span class="num">1</span>What does that mean for their piece of the built environment?</li>
    <li><span class="num">2</span>Why should they care?</li>
    <li><span class="num">3</span>Is it too late for them to get on board?</li>
    <li><span class="num">4</span>Is this a justifiable investment or a waste of time, money and effort?</li>
    <li><span class="num">5</span>Is being “smart” only focused on technologies?</li>
    <li><span class="num">6</span>Who is coordinating all this stuff?</li>
  </ol>

  <section class="event-band">
    <p class="event-invite">Join us as we explore how the built environment connects the dots</p>
    <div class="event-item event-date">
      <svg width="56" height="56" viewBox="0 0 56 56" aria-hidden="true">
        <rect x="4" y="10" width="48" height="42" rx="6" fill="none" stroke="#fff" stroke-width="5"/>
        <rect x="4" y="10" width="48" height="12" fill="#fff"/>
        <rect x="14" y="3" width="5" height="12" rx="2" fill="#fff"/><rect x="37" y="3" width="5" height="12" rx="2" fill="#fff"/>
        <g fill="#fff"><rect x="13" y="28" width="7" height="6"/><rect x="25" y="28" width="7" height="6"/><rect x="37" y="28" width="7" height="6"/>
        <rect x="13" y="38" width="7" height="6"/><rect x="25" y="38" width="7" height="6"/><rect x="37" y="38" width="7" height="6"/></g>
      </svg>
      <span>April 1-3,<br>2020</span>
    </div>
    <div class="event-item event-place">
      <svg width="44" height="58" viewBox="0 0 44 58" aria-hidden="true">
        <path d="M22 2C11 2 2 11 2 22c0 15 20 34 20 34s20-19 20-34C42 11 33 2 22 2z" fill="#fff"/>
        <circle cx="22" cy="21" r="7" fill="var(--green)"/>
      </svg>
      <span>San Antonio,<br>TX</span>
    </div>
  </section>

  <div class="org-mark">
    <span class="org-dot"></span>
    <span class="org-name">I-BemTK</span>
  </div>

  <footer class="site-bar">I-BEMTK.EVENTHUB.ORG</footer>
</main>
</body>
</html>
```